We currently have a good logo and we want business cards that can display our logo but also represent our industry - telecom construction - We are a construction company specializing in telecom construction such as installation of fiber optic cable throughout cities and across the country. Nationwide services
We are large enough to handle most any project yet small enough to be a flexible partner and resource.

Target Market(s)

U.S. based telecom carriers and providers

Industry/Entity Type

Construction

Contact Information for Business Card

Business cards should include our logo, phone number and website address. Also, including some information as to our core services would be good.

Colors

Designer to choose colors to be used in the design.

Requirements
Must have
• Colors based on logo
• Must use our logo
• Logo, name, email, website address, phone number
• Tovek Subterra
• Brent Dacosta
• Director of Business Development
• (913) 555-0187
• www.tovekgrid.example
Nice to have
• Construction services including:
• Small Cell Construction
• Boring/Drilling
• Plowing / Trenching
• Conduit installation
• Fiber pulling
• splicing
• building entries
• Aerial construction
• Aerial Make Ready
• Make Ready Engineering
Should not have
• We are open to ideas

```html
<!DOCTYPE html>
<html lang="en">
<head>
<meta charset="utf-8">
<title>Tovek Subterra — Business Card</title>
<link rel="stylesheet" href="https://fonts.googleapis.com/css2?family=Oswald:wght@500;700&family=Roboto:wght@400;500&display=swap">
<style>
  :root {
    --card-white: #ffffff;
    --swoosh-black: #0d0d0d;
    --swoosh-grey: #3a3a3a;
    --swoosh-sheen: #6b6b6b;
    --ink: #000000;
    --ink-soft: #333333;
    --brand-blue: #1f72c9;
  }
  html, body {
    margin: 0;
    padding: 0;
    overflow: hidden;
    background: var(--card-white);
  }
  .card {
    position: relative;
    width: 1200px;
    height: 686px;
    overflow: hidden;
    background: var(--card-white);
  }
  .card-art {
    position: absolute;
    inset: 0;
  }
  .brand-name {
    position: absolute;
    left: 360px;
    top: 138px;
    width: 270px;
    margin: 0;
    text-align: center;
    font-family: "Oswald", sans-serif;
    font-weight: 700;
    font-size: 56px;
    line-height: 1.05;
    letter-spacing: 1px;
    text-transform: uppercase;
    color: var(--brand-blue);
  }
  .contact-list {
    position: absolute;
    left: 102px;
    top: 429px;
    margin: 0;
    padding: 0;
    list-style: none;
  }
  .contact-list li {
    display: flex;
    align-items: center;
    height: 26px;
    margin-bottom: 17.5px;
    font-family: "Roboto", sans-serif;
    font-weight: 400;
    font-size: 19px;
    color: var(--ink-soft);
    white-space: nowrap;
  }
  .contact-list svg {
    flex: none;
    display: block;
    width: 26px;
    height: 26px;
    margin-right: 16px;
  }
  .person {
    position: absolute;
    left: 520px;
    top: 428px;
    margin: 0;
  }
  .person-name {
    margin: 0;
    font-family: "Oswald", sans-serif;
    font-weight: 700;
    font-size: 34px;
    line-height: 1.1;
    text-transform: uppercase;
    color: var(--ink);
  }
  .person-title {
    margin: 4px 0 0;
    font-family: "Oswald", sans-serif;
    font-weight: 500;
    font-size: 19px;
    line-height: 1.2;
    color: var(--brand-blue);
  }
</style>
</head>
<body>
<main class="card">
  <svg class="card-art" width="1200" height="686" viewBox="0 0 1200 686" xmlns="http://www.w3.org/2000/svg">
    <defs>
      <linearGradient id="swoosh-top" x1="0" y1="0" x2="1" y2="1">
        <stop offset="0" stop-color="var(--swoosh-black)"/>
        <stop offset="0.6" stop-color="var(--swoosh-grey)"/>
        <stop offset="1" stop-color="var(--swoosh-black)"/>
      </linearGradient>
      <linearGradient id="swoosh-bottom" x1="1" y1="0" x2="0" y2="1">
        <stop offset="0" stop-color="var(--swoosh-black)"/>
        <stop offset="0.5" stop-color="var(--swoosh-grey)"/>
        <stop offset="1" stop-color="var(--swoosh-black)"/>
      </linearGradient>
    </defs>

    <path class="swoosh swoosh-top" d="M0 0 H470 C300 40 110 120 0 235 Z" fill="url(#swoosh-top)"/>
    <path class="swoosh-sheen" d="M0 150 C120 70 260 20 400 0" fill="none" stroke="var(--swoosh-sheen)" stroke-width="2" opacity="0.6"/>

    <path class="swoosh swoosh-bottom" d="M1200 170 V686 H675 C900 620 1110 430 1200 170 Z" fill="url(#swoosh-bottom)"/>
    <path class="swoosh-sheen" d="M1200 330 C1130 500 990 630 820 686" fill="none" stroke="var(--swoosh-sheen)" stroke-width="2" opacity="0.6"/>

    <line class="ground-line" x1="30" y1="387" x2="1066" y2="387" stroke="var(--ink)" stroke-width="4"/>

    <g class="job-site-illustration" role="img" aria-label="Silhouettes of an excavator digging a trench, underground conduit runs and a pickup truck carrying a fiber cable reel" fill="var(--ink)">
      <rect x="150" y="196" width="165" height="144"/>
      <rect x="233" y="329" width="397" height="41" opacity="0.12"/>
      <rect x="730" y="186" width="326" height="180"/>
    </g>
  </svg>

  <h1 class="brand-name">Tovek<br>Subterra</h1>

  <div class="person">
    <p class="person-name">Brent Dacosta</p>
    <p class="person-title">Director of Business Development</p>
  </div>

  <ul class="contact-list">
    <li>
      <svg viewBox="0 0 26 26" aria-hidden="true"><circle cx="13" cy="13" r="13" fill="var(--ink)"/><path d="M9 6.5 L11 9.5 L9.8 11 C10.6 13 12.5 15 14.8 16.2 L16.4 15 L19.5 17 L18 19.5 C13 19.5 6.5 13 6.5 8 Z" fill="var(--card-white)"/></svg>
      (913) 555-0187
    </li>
    <li>
      <svg viewBox="0 0 26 26" aria-hidden="true"><circle cx="13" cy="13" r="13" fill="var(--ink)"/><path d="M13 5.5 C9.8 5.5 7.8 7.8 7.8 10.6 C7.8 14 13 20.5 13 20.5 C13 20.5 18.2 14 18.2 10.6 C18.2 7.8 16.2 5.5 13 5.5 Z" fill="var(--card-white)"/><circle cx="13" cy="10.6" r="2" fill="var(--ink)"/></svg>
      Nationwide Services
    </li>
    <li>
      <svg viewBox="0 0 26 26" aria-hidden="true"><circle cx="13" cy="13" r="13" fill="var(--ink)"/><path d="M13 6 L20 12.5 H18 V19.5 H14.8 V15.5 H11.2 V19.5 H8 V12.5 H6 Z" fill="var(--card-white)"/></svg>
      4120 Corrin Way, Overland Park, KS
    </li>
    <li>
      <svg viewBox="0 0 26 26" aria-hidden="true"><circle cx="13" cy="13" r="13" fill="var(--ink)"/><g fill="none" stroke="var(--card-white)" stroke-width="1.4"><circle cx="13" cy="13" r="7"/><ellipse cx="13" cy="13" rx="3" ry="7"/><line x1="6" y1="13" x2="20" y2="13"/><line x1="7.2" y1="9.5" x2="18.8" y2="9.5"/><line x1="7.2" y1="16.5" x2="18.8" y2="16.5"/></g></svg>
      www.tovekgrid.example
    </li>
    <li>
      <svg viewBox="0 0 26 26" aria-hidden="true"><circle cx="13" cy="13" r="13" fill="var(--ink)"/><rect x="6.5" y="8.5" width="13" height="9" fill="var(--card-white)"/><path d="M6.5 8.5 L13 13.8 L19.5 8.5" fill="none" stroke="var(--ink)" stroke-width="1.3"/></svg>
      brent@tovekgrid.example
    </li>
  </ul>
</main>
</body>
</html>
```